Design a Shirt Hang Tag for a brand new streetwear company

We need a hang tag for our apparel. This will be attached and shipper with every shirt, hat, and hoodie. We make streetwear/urban apparel. For a feel of our products see http://loomferal.co

We'd like to see something die cut with a shape that isn't a rectangle.
Looking for a design that embodies "Savage". We are looking for something bold and fun. Our colors usually consist of black. white, and red, but if you feel like doing something else that you feel could fit our brand,go for it. Were savage, we don't want normal.

Target Market(s)

inner city, age 13-29, multi-cultural

Industry/Entity Type

Clothing

Font styles to use
Sans Serif
Other font styles liked:
• artist's choice

Colors
ec1f27
ffffff
000000

Requirements
Must have
• site url: www.loomferal.co
• Band Name: Loom Feral
• Double sided tag
• Die cut design

```html
<!DOCTYPE html>
<html lang="en">
<head>
<meta charset="utf-8">
<title>Loom Feral — Hang Tags</title>
<link href="https://fonts.googleapis.com/css2?family=Antonio:wght@400&display=swap" rel="stylesheet">
<style>
  :root {
    --paper: #ffffff;
    --ink-black: #000000;
    --kraft: #a97c50;
    --accent-red: #ec1f27;
    --white: #ffffff;
    --charcoal: #231f20;
  }
  html, body {
    margin: 0;
    padding: 0;
    overflow: hidden;
    background: var(--paper);
  }
  .canvas {
    position: relative;
    width: 1200px;
    height: 1074px;
    overflow: hidden;
    background: var(--paper);
    font-family: "Antonio", "Arial Narrow", sans-serif;
  }
  .tag-shapes {
    position: absolute;
    inset: 0;
  }
  .tag-front { fill: var(--ink-black); }
  .tag-back { fill: var(--kraft); }
  .punch-hole { fill: var(--paper); }
  .brand-dot { fill: var(--accent-red); }

  .tag-copy {
    position: absolute;
    top: 0;
    width: 300px;
    text-align: center;
  }
  .tag-copy--front { left: 219px; color: var(--white); }
  .tag-copy--back { left: 675px; color: var(--charcoal); }

  .brand-name {
    position: absolute;
    top: 643px;
    left: 0;
    width: 100%;
    margin: 0;
    font-weight: 400;
    font-size: 92px;
    line-height: 81px;
    letter-spacing: 3px;
    text-transform: uppercase;
  }
  .brand-name span {
    display: block;
    height: 81px;
  }
  .site-url {
    position: absolute;
    top: 916px;
    left: 0;
    width: 100%;
    margin: 0;
    font-size: 25px;
    line-height: 34px;
    letter-spacing: 1px;
    text-transform: uppercase;
  }
</style>
</head>
<body>
<main class="canvas">
  <svg class="tag-shapes" width="1200" height="1074" viewBox="0 0 1200 1074" aria-hidden="true">
    <defs>
      <path id="spray-can-tag" d="M300,100 Q300,83 317,83 H421 Q438,83 438,100 V172 H516 Q538,172 538,194 V210 H558 Q580,210 580,232 V932 C580,1005 158,1005 158,932 V232 Q158,210 180,210 H199 V194 Q199,172 221,172 H300 Z"/>
    </defs>

    <g class="tag tag--front">
      <use href="#spray-can-tag" class="tag-front"/>
      <circle class="punch-hole" cx="369" cy="134" r="14"/>
      <circle class="brand-dot" cx="369" cy="440" r="46"/>
    </g>

    <g class="tag tag--back" transform="translate(456 2)">
      <use href="#spray-can-tag" class="tag-back"/>
      <circle class="punch-hole" cx="369" cy="132" r="14"/>
      <circle class="brand-dot" cx="369" cy="438" r="46"/>
    </g>
  </svg>

  <section class="tag-copy tag-copy--front">
    <h1 class="brand-name"><span>Loom</span><span>Feral</span></h1>
    <p class="site-url">www.loomferal.co</p>
  </section>

  <section class="tag-copy tag-copy--back">
    <h2 class="brand-name"><span>Loom</span><span>Feral</span></h2>
    <p class="site-url">www.loomferal.co</p>
  </section>
</main>
</body>
</html>
```